Business Consultancy Wordpress Design

Small business analysis consultancy.

Looking for a bold, clean design for Wordpress. Final site will only be a few pages, some contact information, services provided and a little background information. Potentially a blog.

Colours to be as per logo, with either black or white as the main colour.

Link is www.halvicadvisory.com

More details to be included in the best few days

Name - Halvic Consulting
Provides - Project Consultancy
Updates

Project Deadline Extended
Reason: I am going to be on holiday with little access to the web over 28/02 - 05/03 and am therefore extending the deadline

Target Market(s)

Business professionals

Industry/Entity Type

Business

Colors

Designer to choose colors to be used in the design.

Requirements
Must have
• Must contain the logo in the header
Footer must fit a 3 column layout in wordpress

Business style, royalty free stock images
Nice to have
• Would like the 1 or 2 column wordpress style layout
Should not have
• must not be blog or magazine style layout or look and feel

```html
<!DOCTYPE html>
<html lang="en">
<head>
<meta charset="utf-8">
<title>Halvic Consulting – Homepage Designs</title>
<link href="https://fonts.googleapis.com/css2?family=Open+Sans:wght@300;400;600&display=swap" rel="stylesheet">
<style>
:root{
  --blue:#1a9ad6;
  --green:#6cb33f;
  --ink:#333;
  --muted:#7a7a7a;
  --page:#f4f4f4;
  --header:#e6e6e6;
  --footer:#111;
  --footer-deep:#050505;
  --white:#fff;
  --wall:#c4c4c4;
  --suit:#1f1f22;
}
*{box-sizing:border-box;margin:0;padding:0}
html,body{width:1200px;height:900px;overflow:hidden;background:var(--white)}
body{font-family:"Open Sans",Arial,sans-serif;color:var(--ink)}
.canvas{position:relative;width:1200px;height:900px;overflow:hidden}
.abs{position:absolute}
.layout{position:absolute;top:0;height:900px;background:var(--page);overflow:hidden}
.layout-one{left:0;width:602px}
.layout-two{left:626px;width:567px}

/* image areas: soft gradients in each photo's main tones */
.photo{position:absolute}
.hero{
  background:
    linear-gradient(to bottom,rgba(0,0,0,0) 55%,rgba(15,15,15,.45) 100%),
    radial-gradient(ellipse 30% 55% at 50% 30%,#dadada 0%,rgba(218,218,218,0) 100%),
    radial-gradient(ellipse 22% 60% at 70% 25%,#9a9a9a 0%,rgba(154,154,154,0) 100%),
    linear-gradient(90deg,#1d1d1f 0%,#4a4a4c 8%,#2a2a2d 16%,#3c3c3e 24%,#8d8d8d 33%,var(--wall) 45%,#b0b0b0 58%,#6e6e70 68%,#2c2c2f 78%,#3a3a3c 88%,var(--suit) 100%);
}
.shot-meeting{
  background:
    radial-gradient(ellipse 45% 50% at 30% 35%,#f1f1f1 0%,rgba(241,241,241,0) 100%),
    radial-gradient(ellipse 35% 45% at 80% 75%,#8fa6c4 0%,rgba(143,166,196,0) 100%),
    linear-gradient(160deg,#e8eaec 0%,#b9bcc0 40%,#3a3b40 70%,#22232a 100%);
}
.shot-office{
  background:
    radial-gradient(ellipse 40% 45% at 60% 35%,#fbf4e2 0%,rgba(251,244,226,0) 100%),
    radial-gradient(ellipse 35% 40% at 20% 70%,#d9d9d9 0%,rgba(217,217,217,0) 100%),
    linear-gradient(170deg,#efe6cc 0%,#f4f2ec 40%,#c9cbcf 70%,#5c5e63 100%);
}
.shot-desk{
  background:
    radial-gradient(ellipse 40% 45% at 55% 40%,#f2f3f5 0%,rgba(242,243,245,0) 100%),
    radial-gradient(ellipse 30% 35% at 25% 70%,#2b2d33 0%,rgba(43,45,51,0) 100%),
    linear-gradient(160deg,#eef0f2 0%,#d3d8de 45%,#7b8694 75%,#3e4550 100%);
}
.shot-laptop{
  background:
    radial-gradient(ellipse 40% 40% at 70% 65%,#bfe0a8 0%,rgba(191,224,168,0) 100%),
    radial-gradient(ellipse 35% 40% at 40% 35%,#e6c7b2 0%,rgba(230,199,178,0) 100%),
    linear-gradient(160deg,#fafafa 0%,#eceff2 45%,#a9b6c6 80%,#6a7f9a 100%);
}
.shot-phone{
  background:
    radial-gradient(ellipse 38% 22% at 55% 22%,#e7ecf0 0%,rgba(231,236,240,0) 100%),
    radial-gradient(ellipse 26% 30% at 50% 62%,#c79a7c 0%,rgba(199,154,124,0) 100%),
    radial-gradient(ellipse 22% 10% at 55% 48%,#0c0c0c 0%,rgba(12,12,12,0) 100%),
    linear-gradient(135deg,#3a3e44 0%,#23262b 45%,#17191c 100%);
}
.framed{border:1px solid #cccccc}

.ribbon{position:absolute;background:#1e1e1e;color:var(--white);font-size:14px;font-weight:400;line-height:18px;padding:6px 44px;transform:rotate(-30deg);white-space:nowrap}
.dots{position:absolute;display:flex;gap:3px}
.dots span{width:5px;height:5px;border-radius:50%;border:1px solid #222}
.dots span.on{background:#222}
.brand{position:absolute;display:flex;align-items:center;gap:7px;color:#555;font-weight:400;letter-spacing:.3px;white-space:nowrap}
.brand-mark{border-radius:50%;background:var(--blue)}
.nav-plain{position:absolute;font-size:7px;color:var(--muted)}
.nav-plain a{color:inherit;text-decoration:none;position:absolute;white-space:nowrap}
.nav-plain a.current{color:#2a6f8a;text-decoration:underline}
.nav-pill{position:absolute;display:flex;background:var(--blue);border-radius:2px}
.nav-pill a{color:var(--white);font-size:6.5px;text-decoration:none;padding:0 9px;line-height:17px;border-right:1px solid rgba(255,255,255,.25);white-space:nowrap}
.nav-pill a:last-child{border-right:0}
.heading{position:absolute;font-weight:400;color:#333;white-space:nowrap}
.copy{position:absolute;font-size:7.2px;line-height:15.2px;color:#8a8a8a}
.card-title{position:absolute;font-size:7px;color:#333;white-space:nowrap}
.card-copy{position:absolute;font-size:5.5px;line-height:8.4px;color:var(--muted)}
.btn{position:absolute;background:var(--blue);color:var(--white);font-size:5.5px;display:flex;align-items:center;justify-content:center;white-space:nowrap}
.blog-panel{position:absolute;left:395px;top:314px;width:158px;height:356px;border:1px solid #cfcfcf;background:#f7f7f7}
.blog-panel h3{height:22px;background:var(--header);border-bottom:1px solid #cfcfcf;font-size:10px;font-weight:400;text-align:center;line-height:22px;color:#555}
.blog-item{position:absolute;left:5px;width:148px;height:30px}
.blog-item .photo{left:0;top:0;width:31px;height:26px}
.blog-item p{position:absolute;left:45px;top:0;font-size:5px;line-height:7px;color:#222;width:104px}
.blog-item .date{position:absolute;left:45px;top:19px;font-size:4.5px;font-weight:600;color:#222;display:flex;align-items:center;gap:4px;white-space:nowrap}
.ico{display:inline-block;width:9px;height:9px;background:#222}
.ico.green{background:var(--green)}
.footer{position:absolute;left:0;width:100%;background:var(--footer);color:var(--white)}
.footer h4{position:absolute;font-size:5.5px;font-weight:600;white-space:nowrap}
.footer ul{position:absolute;list-style:none;font-size:5.5px;line-height:11.3px;white-space:nowrap}
.footer p{position:absolute;font-size:5.5px;line-height:7.4px}
.footer-base{position:absolute;left:0;width:100%;height:16px;background:var(--footer-deep);color:#ddd;font-size:5px;text-align:center;line-height:16px}
.diamond{position:absolute;width:22px;height:22px;background:var(--blue);transform:rotate(45deg);border:2px solid var(--footer)}
.diamond::after{content:"";position:absolute;left:7px;top:7px;width:6px;height:6px;border-left:1.5px solid var(--white);border-top:1.5px solid var(--white)}
.topbar{position:absolute;left:0;top:0;width:100%;height:16px;background:#0d0d0d;color:var(--white);font-size:6.5px}
.topbar span{white-space:nowrap}
.social{position:absolute;width:11px;height:11px;top:2px}
.meta{position:absolute;height:14px;display:flex;align-items:center;gap:5px;font-size:5px;font-weight:600;border-bottom:2px solid #bbb;width:107px;white-space:nowrap}
</style>
</head>
<body>
<div class="canvas">

  <section class="layout layout-one">
    <div class="abs" style="left:0;top:0;width:602px;height:4px;background:#111"></div>
    <header class="abs" style="left:0;top:4px;width:602px;height:39px;background:var(--header)">
      <div class="brand" style="left:47px;top:9px;font-size:14.5px">
        <span class="brand-mark" style="width:20px;height:20px"></span>HALVIC CONSULTING
      </div>
      <nav class="nav-plain" style="left:0;top:15px">
        <a class="current" style="left:336px">HOME</a>
        <a style="left:373px">ABOUT US</a>
        <a style="left:423px">SERVICES</a>
        <a style="left:470px">BLOGE</a>
        <a style="left:512px">CONTACT US</a>
      </nav>
    </header>
    <div class="photo hero" style="left:0;top:43px;width:602px;height:209px" role="img" aria-label="Business team in suits with two colleagues shaking hands in front of a world map wall"></div>
    <div class="ribbon" style="left:-30px;top:88px">HomePage Design 1</div>
    <div class="dots" style="left:288px;top:262px"><span></span><span class="on"></span><span class="on"></span></div>

    <h1 class="heading" style="left:46px;top:310px;font-size:15px;font-weight:300">Created to promote your business</h1>
    <p class="copy" style="left:46px;top:342px;width:326px">Lorem ipsum dolor sit amet, consectetur adipiscing elit. Nullam condimentum leo felis, ut ali­quet nisi lobortis ac. Nulla ipsum erat, mollis sit amet est sed, commodo accumsan magna. Morbi a lectus rhoncus odio sollicitudin rhoncus dictum vel turpis. Curabitur luctus lobortis hendrerit Lorem ipsum dolor sit amet, con ectetur adipiscing elit. Nullam condimentum leo felis, ut aliquet nisi lobortis ac. Nulla ipsum erat, mollis sit amet est sed, commodo accumsan magna. Morbi a lectus rhoncus odio sollicitudin rhoncus dictum</p>

    <h2 class="heading" style="left:46px;top:452px;font-size:15px;font-weight:300">Featured Update</h2>
    <div class="photo shot-meeting framed" style="left:47px;top:492px;width:158px;height:97px" role="img" aria-label="Colleagues in a meeting around a laptop"></div>
    <div class="card-title" style="left:47px;top:601px">BEST PROJECT OF THIS THEME</div>
    <p class="card-copy" style="left:47px;top:617px;width:160px">Lorem ipsum dolor sit amet, consectetur adipiscing lobortis ac. Nulla ipsum erat, mollis sit amet est sed, commodo accumsan magna. Morbi a lectus rhoncus odio sollicitudin rhoncus dictum vel turpis. Curabitur luctus lobortis</p>
    <div class="btn" style="left:47px;top:658px;width:45px;height:14px">VIEW DETAILS</div>

    <div class="photo shot-office framed" style="left:220px;top:492px;width:158px;height:97px" role="img" aria-label="Woman working at a computer in a bright open office"></div>
    <div class="card-title" style="left:220px;top:601px">BEST PROJECT OF THIS THEME</div>
    <p class="card-copy" style="left:220px;top:617px;width:160px">Lorem ipsum dolor sit amet, consectetur adipiscing lobortis ac. Nulla ipsum erat, mollis sit amet est sed, commodo accumsan magna. Morbi a lectus rhoncus odio sollicitudin rhoncus dictum vel turpis.</p>
    <div class="btn" style="left:220px;top:658px;width:45px;height:14px">VIEW DETAILS</div>

    <aside class="blog-panel">
      <h3>From The Blog</h3>
      <div class="blog-item" style="top:40px"><div class="photo shot-meeting" role="img" aria-label="Team at a desk"></div><p>Lorem Ipsum is simply dummy text of the printing and typesetting industry.</p><span class="date"><i class="ico"></i>September 16, 2013</span></div>
      <div class="blog-item" style="top:78px"><div class="photo shot-meeting" role="img" aria-label="Team at a desk"></div><p>Lorem Ipsum is simply dummy text of the printing and typesetting industry.</p><span class="date"><i class="ico"></i>September 16, 2013</span></div>
      <div class="blog-item" style="top:116px"><div class="photo shot-desk" role="img" aria-label="Office meeting"></div><p>Lorem Ipsum is simply dummy text of the printing and typesetting industry.</p><span class="date"><i class="ico"></i>September 16, 2013</span></div>
      <div class="blog-item" style="top:154px"><div class="photo shot-laptop" role="img" aria-label="Colleagues at a laptop"></div><p>Lorem Ipsum is simply dummy text of the printing and typesetting industry.</p><span class="date"><i class="ico"></i>September 16, 2013</span></div>
      <div class="blog-item" style="top:192px"><div class="photo shot-meeting" role="img" aria-label="Team at a desk"></div><p>Lorem Ipsum is simply dummy text of the printing and typesetting industry.</p><span class="date"><i class="ico"></i>September 16, 2013</span></div>
      <div class="blog-item" style="top:230px"><div class="photo shot-meeting" role="img" aria-label="Team at a desk"></div><p>Lorem Ipsum is simply dummy text of the printing and typesetting industry.</p><span class="date"><i class="ico"></i>September 16, 2013</span></div>
      <div class="blog-item" style="top:268px"><div class="photo shot-desk" role="img" aria-label="Office meeting"></div><p>Lorem Ipsum is simply dummy text of the printing and typesetting industry.</p><span class="date"><i class="ico"></i>September 16, 2013</span></div>
      <div class="blog-item" style="top:306px"><div class="photo shot-laptop" role="img" aria-label="Colleagues at a laptop"></div><p>Lorem Ipsum is simply dummy text of the printing and typesetting industry.</p><span class="date"><i class="ico"></i>September 16, 2013</span></div>
    </aside>

    <footer class="footer" style="top:744px;height:156px">
      <div class="abs" style="left:56px;top:-2px;width:492px;height:4px;background:#000"></div>
      <div class="diamond" style="left:292px;top:-12px"></div>
      <h4 style="left:65px;top:40px">ABOUT MARLOW APPAREL</h4>
      <p style="left:65px;top:56px;width:112px">By subscribing to our mailing list you will always be update with the latest news from us. By subscribing to our mailing list you will always be update with the latest news from us.</p>
      <h4 style="left:191px;top:40px">MEN'S ACCESSORIES</h4>
      <ul style="left:191px;top:53px"><li>SUN GLASSES</li><li>HATS &amp; CAPS</li><li>WALLETS</li><li>WATCHES</li></ul>
      <h4 style="left:275px;top:40px">WOMEN ACCESSORIES</h4>
      <ul style="left:275px;top:53px"><li>SUN GLASSES</li><li>HATS &amp; CAPS</li><li>WALLETS</li><li>WATCHES</li></ul>
      <h4 style="left:359px;top:40px">NEW ARRIVALS</h4>
      <ul style="left:359px;top:53px"><li>SUN GLASSES</li><li>HATS &amp; CAPS</li><li>WALLETS</li><li>WATCHES</li></ul>
      <h4 style="left:443px;top:40px">CONTACT US</h4>
      <p style="left:443px;top:56px;width:150px">T (041) 555-010-222<br>Email: sales@halvicadvisory.com<br><br>Your Company LTD<br>Street nr 48, 5510482, Dayton, US</p>
      <div class="footer-base" style="top:140px">© 2014 Halvic Consulting . All Rights Reserved</div>
    </footer>
  </section>

  <section class="layout layout-two">
    <div class="topbar">
      <svg class="abs" style="left:48px;top:4px" width="6" height="8" viewBox="0 0 6 8"><rect x=".5" y=".5" width="5" height="7" rx="1" fill="none" stroke="#fff"/></svg>
      <span class="abs" style="left:57px;top:3px">1(800)55501234</span>
      <svg class="abs" style="left:110px;top:5px" width="8" height="6" viewBox="0 0 8 6"><rect x=".5" y=".5" width="7" height="5" fill="none" stroke="#fff"/><path d="M.5 .5 4 3.5 7.5 .5" fill="none" stroke="#fff"/></svg>
      <span class="abs" style="left:121px;top:3px">hello@halvicmail.com</span>
      <span class="social" style="left:459px;background:#3b5a98"></span>
      <span class="social" style="left:476px;background:#d5412f"></span>
      <span class="social" style="left:493px;background:#2ca7e0"></span>
      <span class="social" style="left:510px;background:#cb2027"></span>
    </div>
    <header class="abs" style="left:0;top:16px;width:567px;height:37px;background:#f6f6f6">
      <div class="brand" style="left:48px;top:10px;font-size:13.5px">
        <span class="brand-mark" style="width:18px;height:18px"></span>HALVIC CONSULTING
      </div>
      <nav class="nav-pill" style="left:243px;top:11px">
        <a>HOME</a><a>ABOUT US</a><a>SERVICES</a><a>OUR TEME</a><a>BLOG</a><a>CONTACT US</a>
      </nav>
    </header>
    <div class="photo hero" style="left:0;top:53px;width:567px;height:195px" role="img" aria-label="Business team in suits with two colleagues shaking hands in front of a world map wall"></div>
    <div class="ribbon" style="left:-22px;top:98px">HomePage Design 2</div>
    <div class="dots" style="left:273px;top:258px"><span class="on"></span><span class="on"></span><span class="on"></span></div>

    <h1 class="heading" style="left:47px;top:290px;font-size:13.5px;font-weight:300">Created to promote your business</h1>
    <p class="copy" style="left:47px;top:320px;width:266px;line-height:14.5px;font-size:7px">Lorem ipsum dolor sit amet, consectetur adipiscing elit. Nullam condimentum leo felis, ut aliquet nisi lobortis ac. Nulla ipsum erat, mollis sit amet est sed, com­modo accumsan magna. Morbi a lectus rhoncus odio sollicitudin rhoncus dictum vel turpis. Curabitur luctus lobortis hendrerit Lorem ipsum dolor sit amet, con ectetur adipiscing elit. Nullam condimentum leo felis, ut aliquet nisi lobortis ac. Nulla ipsum erat, mollis sit amet est sed, commodo accumsan magna. Morbi a lectus rhoncus odio sollicitudin rhoncus dictum</p>
    <div class="photo shot-phone" style="left:354px;top:294px;width:166px;height:123px" role="img" aria-label="Hand holding a phone with a world map and airplane floating above it"></div>

    <h2 class="heading" style="left:0;width:567px;text-align:center;top:460px;font-size:13px">BLOG</h2>
    <p class="abs" style="left:0;width:567px;text-align:center;top:480px;font-size:6.5px;color:#444">For further details on our existing projects see the Projects section.</p>

    <div class="photo shot-meeting framed" style="left:47px;top:522px;width:107px;height:80px" role="img" aria-label="Colleagues in a meeting around a laptop"></div>
    <div class="card-title" style="left:47px;top:615px">BEST PROJECT OF THIS THEME</div>
    <div class="meta" style="left:47px;top:633px"><i class="ico green"></i>September 16, 2013 <i class="ico green" style="margin-left:8px"></i>(15)</div>
    <p class="card-copy" style="left:47px;top:657px;width:110px;line-height:10.5px;font-size:6px">Lorem ipsum dolor sit amet, consectetur amet, consectetur</p>
    <div class="btn" style="left:46px;top:684px;width:109px;height:14px;font-size:6px">VIEW DETAILS</div>

    <div class="photo shot-office framed" style="left:170px;top:522px;width:107px;height:80px" role="img" aria-label="Woman working at a computer in a bright open office"></div>
    <div class="card-title" style="left:170px;top:615px">BEST PROJECT OF THIS THEME</div>
    <div class="meta" style="left:170px;top:633px"><i class="ico green"></i>September 16, 2013 <i class="ico green" style="margin-left:8px"></i>(15)</div>
    <p class="card-copy" style="left:170px;top:657px;width:110px;line-height:10.5px;font-size:6px">Lorem ipsum dolor sit amet, consectetur amet, consectetur</p>
    <div class="btn" style="left:169px;top:684px;width:109px;height:14px;font-size:6px">VIEW DETAILS</div>

    <div class="photo shot-desk framed" style="left:292px;top:522px;width:107px;height:80px" role="img" aria-label="Two colleagues at a desktop computer"></div>
    <div class="card-title" style="left:292px;top:615px">BEST PROJECT OF THIS THEME</div>
    <div class="meta" style="left:292px;top:633px"><i class="ico green"></i>September 16, 2013 <i class="ico green" style="margin-left:8px"></i>(15)</div>
    <p class="card-copy" style="left:292px;top:657px;width:110px;line-height:10.5px;font-size:6px">Lorem ipsum dolor sit amet, consectetur amet, consectetur</p>
    <div class="btn" style="left:291px;top:684px;width:109px;height:14px;font-size:6px">VIEW DETAILS</div>

    <div class="photo shot-laptop framed" style="left:415px;top:522px;width:107px;height:80px" role="img" aria-label="Two colleagues working together at a laptop"></div>
    <div class="card-title" style="left:415px;top:615px">BEST PROJECT OF THIS THEME</div>
    <div class="meta" style="left:415px;top:633px"><i class="ico green"></i>September 16, 2013 <i class="ico green" style="margin-left:8px"></i>(15)</div>
    <p class="card-copy" style="left:415px;top:657px;width:110px;line-height:10.5px;font-size:6px">Lorem ipsum dolor sit amet, consectetur amet, consectetur</p>
    <div class="btn" style="left:414px;top:684px;width:109px;height:14px;font-size:6px">VIEW DETAILS</div>

    <footer class="footer" style="top:752px;height:148px">
      <div class="abs" style="left:56px;top:-2px;width:461px;height:4px;background:var(--green)"></div>
      <div class="diamond" style="left:277px;top:-12px"></div>
      <h4 style="left:64px;top:38px">ABOUT MARLOW APPAREL</h4>
      <p style="left:64px;top:53px;width:104px">By subscribing to our mailing list you will always be update with the latest news from us. By subscribing to our mailing list you will always be update with the latest news from us.</p>
      <h4 style="left:182px;top:38px">MEN'S ACCESSORIES</h4>
      <ul style="left:182px;top:50px"><li>SUN GLASSES</li><li>HATS &amp; CAPS</li><li>WALLETS</li><li>WATCHES</li></ul>
      <h4 style="left:261px;top:38px">WOMEN ACCESSORIES</h4>
      <ul style="left:261px;top:50px"><li>SUN GLASSES</li><li>HATS &amp; CAPS</li><li>WALLETS</li><li>WATCHES</li></ul>
      <h4 style="left:340px;top:38px">NEW ARRIVALS</h4>
      <ul style="left:340px;top:50px"><li>SUN GLASSES</li><li>HATS &amp; CAPS</li><li>WALLETS</li><li>WATCHES</li></ul>
      <h4 style="left:419px;top:38px">CONTACT US</h4>
      <p style="left:419px;top:53px;width:145px">T (041) 555-010-222<br>Email: sales@halvicadvisory.com<br><br>Your Company LTD<br>Street nr 48, 5510482, Dayton, US</p>
      <div class="footer-base" style="top:132px">© 2014 Halvic Consulting . All Rights Reserved</div>
    </footer>
  </section>

</div>
</body>
</html>
```